Multi brand diverse distributor requires new business card

We're a distributor representing multiple brands and would like a new business card reflecting our diversity.

We incorporate landscape architecture, environmental engineering and sustainability into construction projects.

KV Group is the company name, and therefore the KV logo should be the primary logo.

Target Market(s)

Engineers, Landscape Architects, Environmental

Contact Information for Business Card

See sample

Colors

Designer to choose colors to be used in the design.

```html
<!DOCTYPE html>
<html lang="en">
<head>
<meta charset="utf-8">
<title>KV Group business card</title>
<link href="https://fonts.googleapis.com/css2?family=Arimo:wght@400;700&display=swap" rel="stylesheet">
<style>
  :root {
    --backdrop: #2a2a2a;
    --card-dark: #141414;
    --card-light: #ffffff;
    --brand-red: #b80c3c;
    --ink: #1a1a1a;
    --muted: #5a5f66;
    --paper-white: #ffffff;
  }
  * { box-sizing: border-box; margin: 0; padding: 0; }
  html, body {
    width: 1200px; height: 1015px; overflow: hidden;
    background: var(--backdrop);
    font-family: "Arimo", Arial, sans-serif;
  }
  .stage { position: relative; width: 1200px; height: 1015px; }
  .card {
    position: absolute; width: 640px; height: 390px;
    box-shadow: 0 14px 30px rgba(0,0,0,.45);
  }
  .card-back { left: 80px; top: 60px; background: var(--card-dark); }
  .card-front { left: 480px; top: 565px; background: var(--card-light); color: var(--ink); }

  .brand { position: absolute; }
  .brand-est {
    position: absolute; right: 0; top: 0;
    font-size: 13px; letter-spacing: 4px; font-weight: 700;
  }
  .brand-name {
    display: block; padding-top: 20px;
    font-weight: 700; font-size: 60px; letter-spacing: 1px;
    color: var(--brand-red); line-height: 1; white-space: nowrap;
  }
  .brand-rule { height: 2px; background: var(--brand-red); margin-top: 10px; }
  .card-back .brand { left: 170px; top: 130px; width: 330px; }
  .card-back .brand-est { color: var(--paper-white); }
  .card-front .brand { right: 36px; top: 30px; width: 300px; }
  .card-front .brand-name { font-size: 54px; }
  .card-front .brand-est { color: var(--ink); }

  .partners {
    position: absolute; right: 30px; top: 150px; width: 160px;
    list-style: none;
    display: flex; flex-direction: column; gap: 14px;
  }
  .partner { display: flex; align-items: center; gap: 8px; font-weight: 700; font-size: 16px; color: var(--muted); }
  .partner-dot { width: 12px; height: 12px; border-radius: 50%; background: var(--muted); flex: none; }

  .person { position: absolute; left: 34px; top: 178px; width: 400px; }
  .person-name { color: var(--brand-red); font-size: 26px; letter-spacing: 1px; font-weight: 400; }
  .person-title { font-size: 17px; margin-top: 2px; }
  .divider { height: 2px; background: var(--brand-red); margin: 10px 0; }
  .contact-grid {
    display: grid; grid-template-columns: auto auto; column-gap: 18px; row-gap: 5px;
    font-size: 16px;
  }
  .contact { display: flex; align-items: center; gap: 7px; white-space: nowrap; }
  .icon { width: 16px; height: 16px; flex: none; }
  .icon * { fill: none; stroke: var(--brand-red); stroke-width: 1.8; }
  .icon .solid { fill: var(--brand-red); stroke: none; }
  .locations { display: flex; gap: 8px; font-size: 18px; line-height: 1.35; }
  .locations .sep { color: var(--brand-red); padding: 0 4px; }
</style>
</head>
<body>
<main class="stage">
  <section class="card card-back" aria-label="Card back">
    <div class="brand">
      <span class="brand-est">EST. 1971</span>
      <span class="brand-name">KV GROUP</span>
      <div class="brand-rule"></div>
    </div>
  </section>

  <section class="card card-front" aria-label="Card front">
    <div class="brand">
      <span class="brand-est">EST. 1971</span>
      <span class="brand-name">KV GROUP</span>
      <div class="brand-rule"></div>
    </div>

    <ul class="partners" aria-label="Represented brands">
      <li class="partner"><span class="partner-dot"></span>Rivanta</li>
      <li class="partner"><span class="partner-dot"></span>Benchora</li>
      <li class="partner"><span class="partner-dot"></span>Tervaloq</li>
      <li class="partner"><span class="partner-dot"></span>Strandelix</li>
    </ul>

    <div class="person">
      <h1 class="person-name">MARCO BELLANDI</h1>
      <p class="person-title">B.Eng (Civil)</p>
      <div class="divider"></div>
      <div class="contact-grid">
        <span class="contact">
          <svg class="icon" viewBox="0 0 16 16"><path d="M3 2l3 3-2 2c1 2 3 4 5 5l2-2 3 3-2 2C7 15 1 9 1 4z"/></svg>
          0400 123 456
        </span>
        <span class="contact">
          <svg class="icon" viewBox="0 0 16 16"><rect x="4" y="1.5" width="8" height="13" rx="1.5"/><path d="M7 12h2"/></svg>
          1300 555 012
        </span>
        <span class="contact">
          <svg class="icon" viewBox="0 0 16 16"><rect x="1.5" y="3.5" width="13" height="9"/><path d="M1.5 3.5l6.5 5 6.5-5"/></svg>
          marco@kv.com.au
        </span>
        <span class="contact">
          <svg class="icon" viewBox="0 0 16 16"><circle cx="8" cy="8" r="6.5"/><path d="M1.5 8h13M8 1.5c-3 3-3 10 0 13M8 1.5c3 3 3 10 0 13"/></svg>
          www.kv.com.au
        </span>
      </div>
      <div class="divider"></div>
      <div class="locations">
        <svg class="icon" viewBox="0 0 16 16" style="width:20px;height:20px;margin-top:4px"><path class="solid" d="M8 1a5 5 0 0 0-5 5c0 4 5 9 5 9s5-5 5-9a5 5 0 0 0-5-5zm0 7a2 2 0 1 1 0-4 2 2 0 0 1 0 4z"/></svg>
        <p>Harbourton<span class="sep">|</span>Ridgevale<span class="sep">|</span>Eastmere<br>Westcliff<span class="sep">|</span>Northbay</p>
      </div>
    </div>
  </section>
</main>
</body>
</html>
```